Harborline Security and Surveillance Business Card

Business Card Design - Company Name:Freedom Security and SurveillanceWe are a Security Systems Integrator Specializing in Security Systems/ Video Surveillance and Access Control. Our areas of expertise are:Security SystemsVideo SurveillanceAccess ControlFire Alarm SystemsNetwork CablingCellular BoostersMy input is the Front of the Card is: logo, name of Business, My Name, Phone Number, and email.Rear of Card is the 6 areas of expertise, I just dont want the front to be very busy.
Name: Tom Werner
Title: President
Email: tom@harborlinesecsys.example
website: harborlinesecsys.example

```html
<!DOCTYPE html>
<html lang="en">
<head>
<meta charset="utf-8">
<title>Harborline Security and Surveillance – Business Card</title>
<link href="https://fonts.googleapis.com/css2?family=Open+Sans:wght@400;600;700&display=swap" rel="stylesheet">
<style>
  :root {
    --backdrop: #e4e4e4;
    --card: #232323;
    --brand-blue: #2f6bc4;
    --text-light: #dedede;
    --text-muted: #4d4d4d;
    --emboss: #3a3a3a;
    --rule: #d6d6d6;
  }
  * { margin: 0; padding: 0; box-sizing: border-box; }
  html, body { width: 1200px; height: 800px; overflow: hidden; }
  body {
    background: var(--backdrop);
    font-family: "Open Sans", Arial, sans-serif;
    position: relative;
  }
  .card {
    position: absolute;
    left: 323px;
    width: 554px;
    height: 326px;
    background: var(--card);
    box-shadow: 0 2px 4px rgba(0,0,0,0.35);
  }
  .card--back { top: 68px; }
  .card--front { top: 434px; }

  /* Back side */
  .back-brand {
    position: absolute;
    top: 82px;
    left: 0;
    width: 100%;
    text-align: center;
  }
  .back-brand__mark {
    display: block;
    width: 56px;
    height: 56px;
    margin: 0 auto 14px;
    background: var(--emboss);
  }
  .back-brand__name {
    font-weight: 600;
    font-size: 22px;
    color: var(--emboss);
    letter-spacing: 1px;
  }
  .services {
    position: absolute;
    top: 229px;
    left: 0;
    width: 100%;
    text-align: center;
    font-weight: 700;
    font-size: 14.5px;
    line-height: 23px;
    color: var(--text-muted);
    letter-spacing: 0.3px;
  }

  /* Front side */
  .front-brand {
    position: absolute;
    top: 52px;
    left: 38px;
  }
  .front-brand__mark {
    display: block;
    width: 46px;
    height: 46px;
    margin: 0 0 14px 92px;
    background: var(--brand-blue);
  }
  .front-brand__name {
    font-weight: 600;
    font-size: 13px;
    color: var(--brand-blue);
    white-space: nowrap;
  }
  .person {
    position: absolute;
    right: 45px;
    top: 150px;
    text-align: right;
  }
  .person__name {
    font-weight: 700;
    font-size: 20px;
    line-height: 24px;
    color: var(--brand-blue);
    text-transform: uppercase;
  }
  .person__title {
    font-size: 16px;
    line-height: 20px;
    color: var(--text-light);
  }
  .divider {
    position: absolute;
    top: 199px;
    left: 38px;
    right: 45px;
    height: 2px;
    background: var(--rule);
  }
  .contacts {
    position: absolute;
    top: 214px;
    left: 38px;
    list-style: none;
  }
  .contacts li {
    display: flex;
    align-items: center;
    height: 21.5px;
    font-size: 14px;
    color: var(--text-light);
  }
  .contacts svg {
    width: 14px;
    height: 14px;
    margin-right: 7px;
    fill: var(--brand-blue);
  }
</style>
</head>
<body>

  <section class="card card--back" aria-label="Back of card">
    <div class="back-brand">
      <span class="back-brand__mark"></span>
      <div class="back-brand__name">Harborline Security and Surveillance</div>
    </div>
    <p class="services">
      Security Systems | Video Surveillance | Access Control<br>
      Fire Alarm Systems | Network Cabling | Cellular Boosters
    </p>
  </section>

  <section class="card card--front" aria-label="Front of card">
    <div class="front-brand">
      <span class="front-brand__mark"></span>
      <div class="front-brand__name">Harborline Security and Surveillance</div>
    </div>

    <div class="person">
      <div class="person__name">Tom Werner</div>
      <div class="person__title">President</div>
    </div>

    <div class="divider"></div>

    <ul class="contacts">
      <li>
        <svg viewBox="0 0 14 14" aria-hidden="true"><path d="M4 0h6a1 1 0 0 1 1 1v12a1 1 0 0 1-1 1H4a1 1 0 0 1-1-1V1a1 1 0 0 1 1-1zm0.5 1.5v9.5h5V1.5zM7 11.6a0.8 0.8 0 1 0 0 1.6a0.8 0.8 0 1 0 0-1.6z"/></svg>
        (555) 014-2739
      </li>
      <li>
        <svg viewBox="0 0 14 14" aria-hidden="true"><path d="M0 3h14v8H0zM1 3.8l6 4.2l6-4.2v-0.3H1z" /></svg>
        tom@harborlinesecsys.example
      </li>
      <li>
        <svg viewBox="0 0 14 14" aria-hidden="true"><path d="M7 0a7 7 0 1 0 0 14A7 7 0 1 0 7 0zm0 1.3a5.7 5.7 0 0 1 0 11.4A5.7 5.7 0 0 1 7 1.3zM1.5 6.4h11v1.2h-11zM6.4 1.5h1.2v11H6.4z"/></svg>
        harborlinesecsys.example
      </li>
      <li>
        <svg viewBox="0 0 14 14" aria-hidden="true"><path d="M7 0a5 5 0 0 0-5 5c0 3.6 5 9 5 9s5-5.4 5-9a5 5 0 0 0-5-5zm0 3a2 2 0 1 1 0 4a2 2 0 1 1 0-4z"/></svg>
        Bay Harbor, Oregon 97000, United States
      </li>
    </ul>
  </section>

</body>
</html>
```